Drowning Victims Recovery Website Design

We are working with Bluewake Recovery Dive Team. They provide recovery services for drowning victims so they can be reunited with their loved ones.

Some sites to use for inspiration:

https://cornerstoneplovik.org
https://www.steadfastmend.org
https://www.givingwellspring.org
https://www.pulsaid.ca/en

Thank you for taking the time to consider designing a website for us. We are web developers based in Stockton, CA, USA. Most of our projects go through the same process. Understanding this process may help you win a project with us. We custom-code all of our websites in-house. We don’t have any requirements as to what tools you use for your design, but we prefer Figma files. For any design that we label as four-stars, we send it to the client for review. The client picks the final design they want us to use. Once we complete this process, we will continue to show additional clients all the four-star sites and purchase them later. Your designs will have multiple chances to sell. For better chances of success, we ask that you follow these guidelines.

IMAGES:
If you use any images or icons in the design, we ask that you have a link to the asset so we can purchase the image/icon. Most of the designs we submit do not have the customer’s images on them unless they have some great images. Be creative; show us the feeling you are trying to portray with your image choices. Use any royalty-free site you choose. We subscribe to Varnex and mainly use their images, but we can purchase images outside of Varnex.

PLEASE NOTE: we will not submit designs to clients with watermarks on the images.

FONTS:
We ask that you identify the fonts used in the design. This can be done in a message if you want. We typically use Google Fonts and Varnex Fonts.

CONTENT:
We're always open to different content and ideas. We often submit designs with stock images so the client can see our vision. We typically take pictures after the website launch to use their images with our vision. Lorem Ipsum is fine for paragraphs, but we ask that you write the headers in correct English. We want to be able to show the vision and identify the sections of the website.

INSPIRATION:
We typically add a couple of links in the brief of websites we like to help you get started in your design.

REVISIONS:
We do not often ask for revisions of the designs unless we see something in the design that may not appeal to the client. If there are slight changes that we want to make, we do that in the development process.

FEEDBACK:
We rarely give feedback on designs during the design process. We are working on many website projects and do not have the time to provide feedback. We usually respond if your request is well thought out and asks specific questions, but a note asking “feedback, please” usually goes unanswered.

```html
<!DOCTYPE html>
<html lang="en">
<head>
<meta charset="utf-8">
<title>Bluewake Recovery Dive Team</title>
<link href="https://fonts.googleapis.com/css2?family=Montserrat:wght@600;700;800&family=Mulish:wght@400;600;700&display=swap" rel="stylesheet">
<style>
:root{
  --navy:#14263f;
  --navy-deep:#0c1a2e;
  --red:#c8161d;
  --red-dark:#9e0f15;
  --ice:#e6eef7;
  --mist:#f1f3f6;
  --ink:#243447;
  --muted:#5b6878;
  --white:#ffffff;
}
*{box-sizing:border-box;margin:0;padding:0}
html,body{width:1200px;height:4236px;overflow:hidden}
body{font-family:"Mulish",Arial,sans-serif;color:var(--ink);background:var(--white);position:relative}
h1,h2,h3,h4,.btn,.nav a,.tab,.stat-num{font-family:"Montserrat",Arial,sans-serif}
section,header,footer{position:absolute;left:0;width:1200px}
.btn{display:inline-flex;align-items:center;gap:8px;background:var(--red);color:var(--white);font-weight:700;font-size:13px;letter-spacing:.5px;padding:12px 22px;border-radius:6px;text-transform:uppercase;text-decoration:none}
.btn.small{font-size:11px;padding:9px 16px}
.heading-bar{display:flex;align-items:center;gap:14px;white-space:nowrap}
.heading-bar::before{content:"";width:8px;height:38px;background:var(--red);display:block;flex:none}
.logo{font-family:"Montserrat",Arial,sans-serif;font-weight:800;color:var(--navy);font-size:26px;line-height:1.05;text-transform:uppercase}

/* header */
.site-header{top:0;height:112px;display:flex;align-items:center;padding:0 150px}
.nav{margin-left:auto;display:flex;align-items:center;gap:34px}
.nav a{font-size:14px;font-weight:700;color:var(--navy);text-decoration:none}
.nav a.active{color:var(--red);border-bottom:3px solid var(--red);padding-bottom:6px}

/* hero */
.hero{top:112px;height:548px;background:linear-gradient(115deg,#050d1c 0%,#0a2a52 45%,#0f5e9e 75%,#1e8ad0 100%);color:var(--white)}
.hero-photo{position:absolute;inset:0}
.hero-copy{position:absolute;left:150px;top:80px;width:720px}
.hero h1{font-size:52px;font-weight:800;line-height:1.12;text-transform:uppercase;white-space:nowrap}
.hero h1 span{color:var(--red)}
.hero p{font-size:22px;line-height:1.45;margin:30px 0 34px;max-width:470px}
.dots{position:absolute;left:0;right:0;bottom:26px;display:flex;justify-content:center;gap:10px}
.dots i{width:10px;height:10px;border-radius:50%;border:2px solid var(--white);display:block}
.dots i.on{background:var(--white)}

/* give */
.give{top:660px;height:360px}
.give-card{position:absolute;left:150px;top:70px;width:420px;height:260px;background:var(--navy);border-radius:6px;overflow:hidden;color:var(--white)}
.tabs{display:flex}
.tab{flex:1;text-align:center;font-size:12px;font-weight:700;padding:12px 0;background:#0b182b;text-transform:uppercase}
.tab.active{background:var(--red)}
.give-body{padding:18px 24px}
.give-body h4{font-size:14px;font-weight:600;margin-bottom:12px}
.amounts{display:grid;grid-template-columns:repeat(3,1fr);gap:10px}
.amount{background:var(--white);color:var(--muted);font-size:12px;padding:9px 10px;border-radius:3px}
.amount.wide{grid-column:span 2}
.give-btn{display:block;margin-top:16px;background:var(--red);text-align:center;font-family:"Montserrat",Arial,sans-serif;font-weight:800;padding:12px;border-radius:3px;font-size:16px}
.mission{position:absolute;left:570px;top:70px;width:480px;height:260px;background:var(--ice);padding:38px 40px}
.mission h2{font-size:28px;font-weight:800;color:var(--navy)}
.mission p{margin-top:22px;font-size:17px;line-height:1.55;color:var(--ink)}

/* welcome */
.welcome{top:1020px;height:660px;background:var(--navy);border-radius:0 60px 0 0;color:var(--white)}
.welcome-copy{position:absolute;left:150px;top:60px;width:500px}
.welcome h2{font-size:26px;font-weight:800;line-height:1.3;text-transform:uppercase;white-space:nowrap}
.welcome p{font-size:15px;line-height:1.6;margin:26px 0 28px;color:#d5dde8;width:470px}
.stats{position:absolute;left:150px;top:470px;display:flex;gap:20px}
.stat{width:150px;height:88px;background:var(--white);color:var(--navy);padding:14px 16px}
.stat-num{font-size:28px;font-weight:800}
.stat span{font-size:13px;display:block;margin-top:2px}
.welcome-photo{position:absolute;left:690px;top:110px;width:360px;height:480px;border-radius:6px;background:linear-gradient(180deg,#e98a3c 0%,#b2452a 40%,#3a2a30 75%,#1a1c26 100%)}

/* resources */
.resources{top:1680px;height:460px}
.resources-photo{position:absolute;left:150px;top:90px;width:420px;height:290px;border-radius:6px;background:linear-gradient(135deg,#6f8a5c 0%,#a7a088 45%,#d9c7aa 100%)}
.resources-copy{position:absolute;left:640px;top:80px;width:430px}
.resources h2{font-size:25px;font-weight:800;color:var(--navy)}
.resources p{font-size:16px;line-height:1.55;margin:20px 0 22px;width:410px}
.res-icons{display:flex;gap:20px}
.res-item{width:124px;text-align:center;font-size:12px;line-height:1.35;font-weight:700;color:var(--navy)}
.res-item .circle{width:58px;height:58px;border-radius:50%;background:var(--red);margin:0 auto 10px;display:flex;align-items:center;justify-content:center}

/* services */
.services{top:2140px;height:620px;background:radial-gradient(ellipse at 55% 35%,#3c8fd6 0%,#0f4c8a 35%,#06203f 75%,#041428 100%)}
.services h2{position:absolute;left:150px;top:60px;color:var(--white);font-size:32px;font-weight:800}
.service-cards{position:absolute;left:150px;top:380px;display:flex;gap:30px}
.service{width:280px;height:220px;background:var(--white);padding:40px 22px 20px;position:relative}
.service .circle{position:absolute;left:50%;top:-28px;margin-left:-28px;width:56px;height:56px;border-radius:50%;background:var(--red);display:flex;align-items:center;justify-content:center;border:4px solid var(--white)}
.service h3{font-size:15px;font-weight:800;color:var(--navy);margin-bottom:10px}
.service p{font-size:12px;line-height:1.55;color:var(--muted);margin-bottom:14px}

/* testimonials */
.testimonials{top:2760px;height:520px;background:linear-gradient(180deg,#ffffff 0%,#eceef1 40%,#f7f8fa 100%);text-align:center}
.testimonials h2{margin-top:70px;font-size:30px;font-weight:800;color:var(--navy)}
.quote-mark{margin:46px auto 10px;font-family:"Montserrat",Arial,sans-serif;font-size:96px;line-height:.7;color:var(--red);font-weight:800}
.testimonials p{width:760px;margin:20px auto 0;font-size:18px;line-height:1.55;color:var(--ink)}
.testimonials h4{margin-top:30px;font-size:14px;font-weight:800;color:var(--navy)}
.testimonials .dots{bottom:50px}
.testimonials .dots i{border-color:var(--navy)}
.testimonials .dots i.on{background:var(--red);border-color:var(--red)}

/* get involved */
.involved{top:3280px;height:600px;background:linear-gradient(180deg,#f2f5f9 0%,#d6e2ee 100%)}
.involved h2{text-align:center;margin-top:70px;font-size:30px;font-weight:800;color:var(--navy)}
.involve-cards{position:absolute;left:150px;top:150px;display:flex;gap:20px}
.involve{width:290px;height:400px;border-radius:6px;position:relative}
.involve.v1{background:linear-gradient(180deg,#2aa4d8 0%,#0d5e96 60%,#0a3b66 100%)}
.involve.v2{width:280px;background:linear-gradient(180deg,#5e2b1d 0%,#c3542a 50%,#2a1410 100%)}
.involve.v3{background:linear-gradient(180deg,#0a2a6e 0%,#1454b4 55%,#0a1c48 100%)}
.involve .btn{position:absolute;left:22px;bottom:24px}

/* footer */
.site-footer{top:3880px;height:356px;background:var(--navy);color:var(--white)}
.site-footer .logo{position:absolute;left:150px;top:90px;color:var(--white);font-size:34px}
.foot-col{position:absolute;top:50px}
.foot-col h4{font-size:13px;font-weight:800;margin-bottom:18px}
.foot-col li{list-style:none;font-size:13px;line-height:1.9;color:#cdd6e2;display:flex;align-items:center;gap:10px}
.socials{display:flex;gap:10px}
.socials i{width:26px;height:26px;border-radius:50%;border:2px solid var(--white);display:block}
.copyright{position:absolute;left:150px;right:150px;bottom:0;border-top:1px solid #2e4260;text-align:center;font-size:12px;color:#aab6c6;padding:22px 0 26px}
</style>
</head>
<body>

<header class="site-header">
  <div class="logo">Bluewake<br>Recovery</div>
  <nav class="nav">
    <a href="#" class="active">HOME</a>
    <a href="#">ABOUT US</a>
    <a href="#">SERVICES</a>
    <a href="#">BLOG</a>
    <a href="#">CONTACT US</a>
    <a href="#" class="btn small"><svg width="14" height="12" viewBox="0 0 14 12"><path d="M7 11.5 1.3 6A3.2 3.2 0 0 1 7 2a3.2 3.2 0 0 1 5.7 4Z" fill="#fff"/></svg>Donate Today</a>
  </nav>
</header>

<section class="hero">
  <div class="hero-photo" role="img" aria-label="Scuba diver descending through deep blue water with sunlight above"></div>
  <div class="hero-copy">
    <h1>Bringing Closure,<br><span>One Recovery</span> At<br>A Time</h1>
    <p>Compassionate recovery services dedicated to reuniting families with their loved ones</p>
    <a href="#" class="btn small"><svg width="14" height="12" viewBox="0 0 14 12"><path d="M7 11.5 1.3 6A3.2 3.2 0 0 1 7 2a3.2 3.2 0 0 1 5.7 4Z" fill="#fff"/></svg>Donate Today</a>
  </div>
  <div class="dots"><i class="on"></i><i></i><i></i><i></i></div>
</section>

<section class="give">
  <div class="give-card">
    <div class="tabs"><div class="tab active">Give Once</div><div class="tab">Give Monthly</div></div>
    <div class="give-body">
      <h4>Choose an amount to give</h4>
      <div class="amounts">
        <div class="amount">$50.00</div><div class="amount">$100.00</div><div class="amount">$150.00</div>
        <div class="amount">$200.00</div><div class="amount wide">Other Amount</div>
      </div>
      <a class="give-btn">GIVE</a>
    </div>
  </div>
  <div class="mission">
    <h2 class="heading-bar">OUR MISSION</h2>
    <p>Reuniting families with their loved ones through expert recovery services. <strong>Bluewake Recovery Dive Team</strong> is dedicated to providing compassionate and professional support in the most challenging times</p>
  </div>
</section>

<section class="welcome">
  <div class="welcome-copy">
    <h2>Welcome to<br>Bluewake Recovery Dive Team</h2>
    <p>Bluewake Recovery Dive Team was founded with a singular purpose: to assist families and communities during their most difficult moments. With years of experience and a commitment to professionalism, we work tirelessly to recover drowning victims and provide closure for their loved ones.</p>
    <a href="#" class="btn small">Read More</a>
  </div>
  <div class="stats">
    <div class="stat"><div class="stat-num">100+</div><span>Recoveries Completed</span></div>
    <div class="stat"><div class="stat-num">10+</div><span>Years of Experience</span></div>
    <div class="stat"><div class="stat-num">20</div><span>Service Areas Covered</span></div>
  </div>
  <div class="welcome-photo" role="img" aria-label="Dive team in gear wading into the water at sunset"></div>
</section>

<section class="resources">
  <div class="resources-photo" role="img" aria-label="Family members embracing outdoors"></div>
  <div class="resources-copy">
    <h2 class="heading-bar">RESOURCES FOR FAMILIES</h2>
    <p>The recovery process can be emotionally taxing. Our team will walk you through every step, from initial contact to final closure, ensuring transparency and support.</p>
    <div class="res-icons">
      <div class="res-item"><div class="circle"><svg width="26" height="24" viewBox="0 0 26 24"><path d="M13 22 3 12a6 6 0 0 1 10-7 6 6 0 0 1 10 7Z" fill="#fff"/></svg></div>Grief Counseling Services</div>
      <div class="res-item"><div class="circle"><svg width="26" height="26" viewBox="0 0 26 26" fill="none" stroke="#fff" stroke-width="2.4"><path d="M13 3v20M5 23h16M4 8h18M4 8l-3 8h6ZM22 8l-3 8h6Z"/></svg></div>Legal Assistance Resources</div>
      <div class="res-item"><div class="circle"><svg width="28" height="24" viewBox="0 0 28 24" fill="#fff"><circle cx="14" cy="6" r="4"/><circle cx="5" cy="9" r="3"/><circle cx="23" cy="9" r="3"/><path d="M7 22a7 7 0 0 1 14 0ZM0 22a5 5 0 0 1 8-4v4ZM28 22a5 5 0 0 0-8-4v4Z"/></svg></div>Local Community Support Groups</div>
    </div>
  </div>
</section>

<section class="services" role="img" aria-label="Divers silhouetted against light shining through the water">
  <h2 class="heading-bar">OUR SERVICES</h2>
  <div class="service-cards">
    <div class="service"><div class="circle"><svg width="22" height="22" viewBox="0 0 22 22" fill="none" stroke="#fff" stroke-width="2.4"><circle cx="11" cy="11" r="8"/><path d="M11 3v16M3 11h16"/></svg></div><h3>RECOVERY SERVICES</h3><p>We specialize in underwater recovery to locate and retrieve drowning victims. Using state-of-the-art equipment and techniques, we aim to provide families with the closure they need.</p><a class="btn small">Read More</a></div>
    <div class="service"><div class="circle"><svg width="18" height="24" viewBox="0 0 18 24"><path d="M9 23S1 13 1 9a8 8 0 0 1 16 0c0 4-8 14-8 14Z" fill="#fff"/><circle cx="9" cy="9" r="3" fill="#c8161d"/></svg></div><h3>SERVICE AREAS</h3><p>We operate across lakes, rivers and coastal waters throughout the region, responding quickly wherever families need our help and support most.</p><a class="btn small">Read More</a></div>
    <div class="service"><div class="circle"><svg width="24" height="22" viewBox="0 0 24 22"><path d="M2 2h20v13H9l-5 5v-5H2Z" fill="#fff"/></svg></div><h3>CONSULTATION SERVICES</h3><p>We offer guidance to families, agencies and communities on recovery planning, water safety and what to expect during every stage of the process.</p><a class="btn small">Read More</a></div>
  </div>
</section>

<section class="testimonials">
  <h2>TESTIMONIALS</h2>
  <div class="quote-mark">&ldquo;</div>
  <p>Lorem ipsum dolor sit amet, consectetur adipiscing elit, sed do eiusmod tempor incididunt ut labore et dolore magna aliqua. Ut enim ad minim veniam, quis nostrud exercitation ullamco laboris nisi ut aliquip ex ea commodo consequat. Duis aute irure dolor in reprehenderit in voluptate velit esse cillum</p>
  <h4>MARIELA D.</h4>
  <div class="dots"><i class="on"></i><i></i><i></i><i></i></div>
</section>

<section class="involved">
  <h2>GET INVOLVED</h2>
  <div class="involve-cards">
    <div class="involve v1" role="img" aria-label="Diver swimming in clear blue water"><a class="btn small">Volunteer Opportunities</a></div>
    <div class="involve v2" role="img" aria-label="Dive team gathered at sunset"><a class="btn small">Donations</a></div>
    <div class="involve v3" role="img" aria-label="Diver training in deep blue water"><a class="btn small">Training Programs</a></div>
  </div>
</section>

<footer class="site-footer">
  <div class="logo">Bluewake<br>Recovery<br>Dive Team</div>
  <div class="foot-col" style="left:460px">
    <h4>CONTACT US</h4>
    <ul>
      <li><svg width="12" height="16" viewBox="0 0 12 16"><path d="M6 15S1 9 1 6a5 5 0 0 1 10 0c0 3-5 9-5 9Z" fill="#fff"/></svg>214 Harbor Lane, Stockton, CA</li>
      <li><svg width="14" height="12" viewBox="0 0 14 12" fill="none" stroke="#fff" stroke-width="1.6"><rect x="1" y="1" width="12" height="10"/><path d="m1 1 6 5 6-5"/></svg>info@bluewakerecovery.org</li>
      <li><svg width="14" height="14" viewBox="0 0 14 14"><path d="M3 1 5 4 4 6a8 8 0 0 0 4 4l2-1 3 2-1 2C6 13 1 8 1 2Z" fill="#fff"/></svg>+1 209 555 0142</li>
    </ul>
  </div>
  <div class="foot-col" style="left:740px">
    <h4>MENU</h4>
    <ul><li>Home</li><li>About Us</li><li>Services</li><li>Blog</li><li>Contact Us</li></ul>
  </div>
  <div class="foot-col" style="left:920px">
    <h4>FOLLOW US</h4>
    <div class="socials"><i></i><i></i><i></i><i></i></div>
  </div>
  <div class="copyright">Copyright © 2025 All Rights Reserved</div>
</footer>

</body>
</html>
```